Customer Dashboard Design for Email Security SaaS

Mailvarden is a commercial email spam filter offered as a SaaS product, built and operated by a small German hosting provider. It protects business email accounts against spam, phishing, scam, and viruses using a multilayer filtering pipeline that combines traditional spam detection with AI-powered classification. The product runs entirely on German infrastructure, ensuring data sovereignty for European customers.

We need a complete redesign of the customer-facing dashboard. This is the web application where paying customers manage their email filtering: view their mail log, check quarantined emails, manage allow/blocklists, configure their settings, and handle their subscription. It is the primary touchpoint between Mailvarden and its customers.

Our customers are system administrators, IT managers at small-to-medium businesses, and operators of small hosting providers. They are technically competent but not designers. They expect professional, efficient tools that respect their time. They typically manage 10–500 email accounts and check the dashboard a few times per week, with heavier use during spam incidents.

We have attached the current mockups which really need to be replaced with something good looking.

Target Market(s)

System administrators, IT managers at small-to-medium businesses, and operators of small hosting providers.

Industry/Entity Type

SaaS

Number of Pages Required

5+ page

```html
<!DOCTYPE html>
<html lang="de">
<head>
<meta charset="utf-8">
<title>Mailvarden – Übersicht</title>
<link rel="stylesheet" href="https://fonts.googleapis.com/css2?family=Montserrat:wght@400;500;700&family=Mulish:wght@400;600;700;800&display=swap">
<style>
:root{
  --bg-main:#141312;
  --bg-header:#1e1c1b;
  --bg-sidebar:#272425;
  --bg-card:#1b1a19;
  --active:#5f4630;
  --accent:#d4913f;
  --green:#34b87b;
  --red:#f01f47;
  --text:#ffffff;
  --muted:#8a8580;
  --border:#44403d;
  --grid:#2a2827;
}
*{margin:0;padding:0;box-sizing:border-box}
html,body{width:1200px;height:1042px;overflow:hidden;background:var(--bg-main);color:var(--text);font-family:'Mulish',sans-serif}
.app{position:relative;width:1200px;height:1042px}
.sidebar{position:absolute;left:0;top:0;width:280px;height:1042px;background:var(--bg-sidebar)}
.brand{position:absolute;left:48px;top:28px;font-family:'Montserrat',sans-serif;font-weight:700;font-size:35px;letter-spacing:.3px}
.nav-active{position:absolute;left:0;top:105px;width:280px;height:66px;background:var(--active)}
.nav-item{position:absolute;left:0;width:280px;height:40px;display:flex;align-items:center;font-family:'Montserrat',sans-serif;font-size:18px}
.nav-item svg{position:absolute;left:58px;width:26px;height:26px;fill:none;stroke:var(--muted);stroke-width:1.6;stroke-linecap:round;stroke-linejoin:round}
.nav-item.is-active svg{stroke:var(--accent)}
.nav-item span{position:absolute;left:119px}
.sidebar-divider{position:absolute;left:0;top:684px;width:280px;height:1px;background:#3a3736}
.section-title{position:absolute;left:64px;top:730px;font-family:'Montserrat',sans-serif;font-size:20px;font-weight:500;letter-spacing:.5px}
.section-link{position:absolute;left:64px;top:775px;font-family:'Montserrat',sans-serif;font-size:18px}
.header{position:absolute;left:280px;top:0;width:920px;height:135px;background:var(--bg-header)}
.greeting{position:absolute;left:55px;top:28px;font-family:'Montserrat',sans-serif;font-weight:700;font-size:42px}
.mode-note{position:absolute;left:55px;top:85px;font-size:19px;color:var(--accent)}
.top-link{position:absolute;left:636px;top:26px;font-family:'Montserrat',sans-serif;font-size:17px}
.top-icon{position:absolute;top:22px;width:28px;height:28px;fill:none;stroke:#fff;stroke-width:1.6;stroke-linecap:round}
.card{position:absolute;border:1px solid var(--border);border-radius:4px;background:var(--bg-card)}
.card.is-highlight{background:var(--accent);border-color:var(--accent)}
.card .label{position:absolute;font-size:19px}
.card .value{position:absolute;font-weight:800;font-size:40px;letter-spacing:-.5px}
.card .sub{position:absolute;font-size:15px}
.card.small .label{font-size:17px;top:21px}
.card.small .value{font-size:35px;top:46px}
.card.small .sub{font-size:14px;top:91px}
.card.wide .label{top:24px}
.card.wide .value{top:46px}
.card.wide .sub{top:102px}
.chart-title{position:absolute;left:324px;top:515px;font-weight:800;font-size:29px}
.chart{position:absolute;left:320px;top:580px;width:811px;height:410px;border:1px solid var(--border);border-radius:4px;background:var(--bg-card)}
.chart svg{position:absolute;left:0;top:0}
.legend-label{position:absolute;top:345px;font-size:17px}
</style>
</head>
<body>
<div class="app">
  <aside class="sidebar">
    <div class="brand">Mailvarden</div>
    <div class="nav-active"></div>
    <div class="nav-item is-active" style="top:120px"><svg viewBox="0 0 26 26"><path d="M3 12 13 3l10 9M6 10v13h5v-7h4v7h5V10"/></svg><span>Übersicht</span></div>
    <div class="nav-item" style="top:182px"><svg viewBox="0 0 26 26"><path d="M5 7h16M5 11h16M5 15h16M5 19h16"/></svg><span>Mail-Log</span></div>
    <div class="nav-item" style="top:245px"><svg viewBox="0 0 26 26"><rect x="3" y="6" width="20" height="15" rx="2"/><path d="m3 8 10 7 10-7"/></svg><span>Postfächer</span></div>
    <div class="nav-item" style="top:307px"><svg viewBox="0 0 26 26"><path d="M13 3 4 6v7c0 5 4 8 9 10 5-2 9-5 9-10V6z"/><path d="m9 13 3 3 5-6"/></svg><span>Allowlist</span></div>
    <div class="nav-item" style="top:370px"><svg viewBox="0 0 26 26"><path d="M13 3 4 6v7c0 5 4 8 9 10 5-2 9-5 9-10V6z"/><path d="M13 9v5M13 17v.5"/></svg><span>Blocklist</span></div>
    <div class="nav-item" style="top:432px"><svg viewBox="0 0 26 26"><circle cx="13" cy="13" r="3.5"/><path d="M13 3v3M13 20v3M3 13h3M20 13h3M6 6l2 2M18 18l2 2M6 20l2-2M18 8l2-2"/><circle cx="13" cy="13" r="7"/></svg><span>Quarantäne</span></div>
    <div class="nav-item" style="top:495px"><svg viewBox="0 0 26 26"><rect x="5" y="12" width="16" height="11" rx="2"/><path d="M8 12V8a5 5 0 0 1 10 0v4"/></svg><span>Einstellungen</span></div>
    <div class="nav-item" style="top:557px"><svg viewBox="0 0 26 26"><rect x="3" y="6" width="20" height="12" rx="1.5"/><circle cx="13" cy="12" r="2.5"/><path d="M4 21h18"/></svg><span>Abrechnung</span></div>
    <div class="sidebar-divider"></div>
    <div class="section-title">VERWALTUNG</div>
    <div class="section-link">Administration</div>
  </aside>

  <header class="header">
    <h1 class="greeting">Guten Tag,</h1>
    <p class="mode-note">Beobachtungsmodus - Mails werden analysiert aber nicht blockiert</p>
    <div class="top-link">Übersicht</div>
    <svg class="top-icon" style="left:742px" viewBox="0 0 28 28"><circle cx="14" cy="8" r="5"/><path d="M3 26v-3c0-4 4-6 11-6s11 2 11 6v3z"/></svg>
    <svg class="top-icon" style="left:784px" viewBox="0 0 28 28"><path d="M24 8A11 11 0 1 0 7 24 10 10 0 0 1 24 8z"/></svg>
    <svg class="top-icon" style="left:825px" viewBox="0 0 28 28"><circle cx="14" cy="14" r="5.5"/><path d="M14 2v3M14 23v3M2 14h3M23 14h3M5.5 5.5l2 2M20.5 20.5l2 2M5.5 22.5l2-2M20.5 7.5l2-2"/></svg>
  </header>

  <section class="card wide is-highlight" style="left:315px;top:193px;width:351px;height:142px">
    <div class="label" style="left:31px">Letzte 24 Stunden</div>
    <div class="value" style="left:30px">0.987</div>
    <div class="sub" style="left:31px">0 zugestellt, 0 abgefangen</div>
  </section>
  <section class="card wide" style="left:690px;top:193px;width:211px;height:142px">
    <div class="label" style="left:51px">7 TAGE</div>
    <div class="value" style="left:50px">1.987</div>
    <div class="sub" style="left:51px">0% zugestellt</div>
  </section>
  <section class="card wide" style="left:924px;top:193px;width:211px;height:142px">
    <div class="label" style="left:56px">7 TAGE</div>
    <div class="value" style="left:55px">2.987</div>
    <div class="sub" style="left:56px">0% zugestellt</div>
  </section>

  <section class="card small" style="left:320px;top:356px;width:189px;height:128px">
    <div class="label" style="left:46px">Spam blockiert</div>
    <div class="value" style="left:45px">1.987</div>
    <div class="sub" style="left:46px">0% zugestellt</div>
  </section>
  <section class="card small" style="left:528px;top:356px;width:189px;height:128px">
    <div class="label" style="left:33px">Phishing erkannt</div>
    <div class="value" style="left:33px">2.987</div>
    <div class="sub" style="left:34px">0% zugestellt</div>
  </section>
  <section class="card small" style="left:735px;top:356px;width:189px;height:128px">
    <div class="label" style="left:25px">Viren abgefangen</div>
    <div class="value" style="left:24px">1.987</div>
    <div class="sub" style="left:25px">0% zugestellt</div>
  </section>
  <section class="card small" style="left:943px;top:356px;width:189px;height:128px">
    <div class="label" style="left:37px">In Quarantäne</div>
    <div class="value" style="left:37px">2.987</div>
    <div class="sub" style="left:38px">0% zugestellt</div>
  </section>

  <h2 class="chart-title">Letzte 30 Tage</h2>
  <section class="chart">
    <svg width="811" height="410" viewBox="0 0 811 410">
      <g stroke="var(--grid)" stroke-width="1">
        <line x1="78" y1="98" x2="754" y2="98"/>
        <line x1="78" y1="198" x2="754" y2="198"/>
        <line x1="78" y1="298" x2="754" y2="298"/>
      </g>
      <g fill="var(--accent)">
        <rect x="125" y="105" width="30" height="193"/><rect x="285" y="105" width="30" height="193"/>
        <rect x="445" y="105" width="30" height="193"/><rect x="604" y="105" width="30" height="193"/>
      </g>
      <g fill="var(--green)">
        <rect x="163" y="147" width="30" height="151"/><rect x="322" y="147" width="30" height="151"/>
        <rect x="482" y="147" width="30" height="151"/><rect x="642" y="147" width="30" height="151"/>
      </g>
      <g fill="var(--red)">
        <rect x="200" y="204" width="30" height="94"/><rect x="360" y="204" width="30" height="94"/>
        <rect x="520" y="204" width="30" height="94"/><rect x="679" y="204" width="30" height="94"/>
      </g>
      <circle cx="56" cy="355" r="10" fill="var(--accent)"/>
      <circle cx="193" cy="355" r="10" fill="var(--green)"/>
      <circle cx="330" cy="355" r="10" fill="var(--red)"/>
      <circle cx="470" cy="355" r="10" fill="var(--red)"/>
    </svg>
    <span class="legend-label" style="left:83px">Akzeptiert</span>
    <span class="legend-label" style="left:217px">Abgelehnt</span>
    <span class="legend-label" style="left:351px">Quarantäne</span>
    <span class="legend-label" style="left:501px">Abgelehnt</span>
  </section>
</div>
</body>
</html>
```